KEV.PRO- Darren Holcombe Fitness- needs a clever business card using the logo, name, info, contact

I need a business card designed for my Online Personal Training company called KEV.PRO, abbreviation for Darren Holcombe Fitness. My company focuses on coaching in personal health and personal growth to unleash your greatest potential. I would like to see designs that use my color scheme of a redish-orange (C:0,M:84,Y:100,K:0), grey, white, black, and my company font is OSWALD. The final design should communicate some aspects of design, health, motivation, growth, in some way. The logo is very important to the company and can be displayed in any of the colors previously mentioned. Must include the company name, my website: www.kev-pro.example , my email: dan@kev-pro.example

Target Market(s)

Personal health, fitness, general public, those who lack knowledge, awareness, and confidence in personal health

Industry/Entity Type

Personal Trainer

Font styles to use
Other font styles liked:
• OSWALD. (Bold, Regular, Light)

Colors
f37122
ffffff
9d9d9d
000000

Requirements
Must have
• Must include the logo, company name, my website: www.kev-pro.example , my email: dan@kev-pro.example
Nice to have
• Variations of the colors scheme of a redish-orange (C:0,M:84,Y:100,K:0), grey, white, black. Logo, card, or text can be in any of these colors.
• Possible quote like "Take control of your personal health to unleash your greatest potential" or "Becoming your strongest self starts with training of the body and mind"

```html
<!DOCTYPE html>
<html lang="en">
<head>
<meta charset="utf-8">
<title>KEV.PRO Business Card</title>
<link href="https://fonts.googleapis.com/css2?family=Oswald:wght@300;400;700&family=Arimo:wght@400&display=swap" rel="stylesheet">
<style>
  :root {
    --brand-orange: #f2441a;
    --card-black: #0a0a0a;
    --ink-white: #ffffff;
    --page-white: #ffffff;
  }
  * { margin: 0; padding: 0; box-sizing: border-box; }
  html, body {
    width: 1200px;
    height: 341px;
    overflow: hidden;
    background: var(--page-white);
  }
  .sheet {
    position: relative;
    width: 1200px;
    height: 341px;
  }
  .card {
    position: absolute;
    top: 0;
    height: 341px;
    background: var(--card-black);
    overflow: hidden;
  }
  .card--front { left: 0; width: 595px; }
  .card--back { left: 606px; width: 594px; }

  /* Front */
  .front-frame {
    position: absolute;
    left: 9px; top: 12px;
    width: 580px; height: 284px;
    border: 4px solid var(--brand-orange);
  }
  .brand-disc {
    position: absolute;
    left: 205px; top: 41px;
    width: 184px; height: 184px;
    border-radius: 50%;
    background: var(--ink-white);
  }
  .front-wordmark {
    position: absolute;
    left: 0; width: 595px;
    top: 228px;
    text-align: center;
    color: var(--ink-white);
    font-family: "Oswald", sans-serif;
  }
  .front-wordmark .name {
    display: block;
    font-weight: 700;
    font-size: 27px;
    line-height: 34px;
  }
  .front-wordmark .sub {
    display: block;
    font-weight: 300;
    font-size: 9px;
    line-height: 11px;
  }
  .quote-band {
    position: absolute;
    left: 12px; top: 293px;
    width: 576px; height: 35px;
    background: var(--brand-orange);
    color: var(--ink-white);
    font-family: "Oswald", sans-serif;
    font-weight: 300;
    font-size: 20px;
    line-height: 35px;
    text-align: center;
    white-space: nowrap;
  }

  /* Back */
  .rule {
    position: absolute;
    background: var(--brand-orange);
  }
  .rule--top { left: 19px; top: 24px; width: 556px; height: 4px; }
  .rule--bottom { left: 19px; top: 315px; width: 556px; height: 4px; }
  .rule--divider { left: 249px; top: 24px; width: 4px; height: 295px; }

  .back-wordmark {
    position: absolute;
    left: 27px; top: 116px;
    width: 200px;
    color: var(--ink-white);
    font-family: "Oswald", sans-serif;
    text-align: center;
  }
  .back-wordmark .name {
    display: block;
    font-weight: 700;
    font-size: 57px;
    line-height: 66px;
    white-space: nowrap;
  }
  .back-wordmark .sub {
    display: block;
    font-weight: 300;
    font-size: 16px;
    line-height: 20px;
    white-space: nowrap;
  }
  .back-wordmark .underline {
    display: block;
    margin: 6px auto 0;
    width: 192px;
    height: 3px;
    background: var(--ink-white);
  }

  .contact {
    position: absolute;
    left: 245px; top: 136px;
    width: 341px;
    list-style: none;
    color: var(--ink-white);
    font-family: "Arimo", sans-serif;
    font-size: 19px;
    line-height: 32px;
    text-align: center;
    white-space: nowrap;
  }
</style>
</head>
<body>
<main class="sheet">
  <section class="card card--front" aria-label="Card front">
    <div class="front-frame"></div>
    <div class="brand-disc" aria-hidden="true"></div>
    <div class="front-wordmark">
      <span class="name">KEV.PRO</span>
      <span class="sub">DARREN HOLCOMBE.FITNESS</span>
    </div>
    <p class="quote-band">Becoming your strongest self starts with training of the body and mind</p>
  </section>

  <section class="card card--back" aria-label="Card back">
    <div class="rule rule--top"></div>
    <div class="rule rule--divider"></div>
    <div class="rule rule--bottom"></div>
    <div class="back-wordmark">
      <span class="name">KEV.PRO</span>
      <span class="sub">DARREN HOLCOMBE.FITNESS</span>
      <span class="underline"></span>
    </div>
    <ul class="contact">
      <li>Website : www.kev-pro.example</li>
      <li>Email &nbsp;: dan@kev-pro.example</li>
    </ul>
  </section>
</main>
</body>
</html>
```